Australian residential property business needs a business card design

I need a business card design for my new business 'Harbour Estate Ventures'. The business will involve house purchases, land development sites, renovation projects, sub-divisions etc. I will be buying property from motivated vendors and working with property investors. I will deal with a wide range of people working in the residential property market including real estate agents, councils, tradespeople, banks, home owners, etc.

I would like something simple, not flashy, but a little bit unique. The colours should be in line with my logo. The business card needs to be professional. I would like something memorable, but not 'busy' or too bright. Not boring. Modern ok.

Target Market(s)

Home owners looking to sell their property, real estate agents, tradespeople (e.g. plumbers, builders, electricians etc), property investors, local councils, and anyone else involved in the residential property industry

Industry/Entity Type

Business

Contact Information for Business Card

I need to include my business name/logo, my name, my title, a PO Box number/address, a mobile number, and an email address.

Font styles to use
Serif

Requirements
Must have
• My business card details listed above.

```html
<!DOCTYPE html>
<html lang="en">
<head>
<meta charset="utf-8">
<title>Harbour Estate Ventures – Business Card</title>
<link rel="stylesheet" href="https://fonts.googleapis.com/css2?family=Source+Serif+4:wght@400;600&display=swap">
<style>
  :root {
    --page-bg: #ecebe7;
    --card-white: #ffffff;
    --card-grey: #ebebeb;
    --brand-green: #1a9a4f;
    --brand-yellow: #f9cf3a;
    --brand-orange: #f0a91f;
    --ink: #333333;
    --ink-soft: #555555;
  }
  * { box-sizing: border-box; margin: 0; padding: 0; }
  html, body {
    width: 1200px; height: 600px; overflow: hidden;
    background: var(--page-bg);
    font-family: "Source Serif 4", Georgia, serif;
  }
  .canvas {
    width: 1200px; height: 600px;
    display: flex; align-items: center; justify-content: center;
  }
  .card {
    position: relative;
    width: 840px; height: 480px;
    background: linear-gradient(120deg, var(--card-white) 40%, var(--card-grey) 100%);
    box-shadow: 0 10px 30px rgba(0,0,0,.18);
    overflow: hidden;
  }
  .card__band {
    position: absolute; left: 0; right: 0; height: 12px;
    background: var(--brand-green);
  }
  .card__band--top { top: 0; }
  .card__band--bottom { bottom: 0; }
  .card__artwork {
    position: absolute; left: 400px; top: 60px;
    width: 440px; height: 380px;
    background: radial-gradient(ellipse at 55% 50%,
      rgba(249,207,58,.55) 0%,
      rgba(240,169,31,.45) 45%,
      rgba(240,169,31,.15) 65%,
      rgba(240,169,31,0) 72%);
  }
  .card__company {
    position: absolute; top: 40px; right: 44px;
    font-size: 28px; font-weight: 400; color: var(--ink);
  }
  .contact {
    position: absolute; left: 400px; top: 108px;
    color: var(--ink);
  }
  .contact__name { font-size: 30px; font-weight: 400; color: var(--brand-green); line-height: 1.1; }
  .contact__title { font-size: 14px; color: var(--ink-soft); margin-bottom: 20px; }
  .contact__address { font-size: 16px; line-height: 1.45; margin-bottom: 22px; }
  .contact__line { display: flex; align-items: center; gap: 8px; font-size: 16px; line-height: 1.6; }
  .contact__icon { width: 14px; height: 14px; flex: none; }
  .lockup {
    position: absolute; left: 56px; bottom: 96px;
    display: flex; align-items: center; gap: 10px;
  }
  .lockup__mark { width: 20px; height: 20px; background: var(--brand-orange); }
  .lockup__name { font-size: 22px; font-weight: 600; color: var(--brand-orange); }
</style>
</head>
<body>
<main class="canvas">
  <article class="card">
    <div class="card__band card__band--top"></div>
    <div class="card__artwork" role="img" aria-label="Yellow island map with a green house illustration"></div>
    <h1 class="card__company">Harbour Estate Ventures</h1>
    <section class="contact">
      <p class="contact__name">Liam Carter</p>
      <p class="contact__title">Director</p>
      <p class="contact__address">PO Box 482<br>Newcastle NSW 2300</p>
      <p class="contact__line">
        <svg class="contact__icon" viewBox="0 0 14 14"><rect x="3" y="1" width="8" height="12" rx="1.5" fill="none" stroke="var(--brand-green)" stroke-width="1.5"/><circle cx="7" cy="11" r="0.9" fill="var(--brand-green)"/></svg>
        0412 555 019
      </p>
      <p class="contact__line">
        <svg class="contact__icon" viewBox="0 0 14 14"><rect x="1" y="3" width="12" height="8" fill="var(--brand-green)"/><path d="M1 3 L7 8 L13 3" fill="none" stroke="#fff" stroke-width="1.2"/></svg>
        liam@harbourestate.com
      </p>
    </section>
    <div class="lockup">
      <span class="lockup__mark"></span>
      <span class="lockup__name">Harbour Estate Ventures</span>
    </div>
    <div class="card__band card__band--bottom"></div>
  </article>
</main>
</body>
</html>
```